LV Business Card NEEDED

Larch Vantage is a finance brokering company that provide lending advise to consumer, business, corporate, and property developer for all their financing needs.

We source and match customer needs in Home Loan, Business Loan, Commercial Property Loan, Assets Finance, and other banking related services. It is a market with full of loans! But we specialise in more complex loan structure and our client base are more business and corporate level. Our suppliers are Banks and large Financial Institution where these business card will go to.

We have a great deal of Asian clients, therefore the card need to also include Chinese language together with English.

Refer to attached file for logo and content requirements.

We are looking for designs with the following ingredients:
* Innovative & Creative
* Professional
* Trust & Security

Please pick colours that will compliment the colours of the company logo.

Please provide a unique design, for example the edge of the card is rounded or corner cut off.

Company logo uploaded.

Please commence submitting your design.

Target Market(s)

Target audiences are businessmen, corporate, and property developer. And also a great deal of Chinese clients.

Industry/Entity Type

Finance

Contact Information for Business Card

Larch Vantage Pty. Ltd.
Morris Pelham
Director
Suite 27, 3-9 Quenby St. Auburn NSW 2144

Requirements
Must have
• Double sided design

```html
<!DOCTYPE html>
<html lang="en">
<head>
<meta charset="utf-8">
<title>Larch Vantage Business Card</title>
<link href="https://fonts.googleapis.com/css2?family=Marcellus&family=Tinos:ital@0;1&family=Noto+Serif+TC:wght@500&display=swap" rel="stylesheet">
<style>
  :root {
    --backdrop: #2b2b2d;
    --navy-deep: #14254a;
    --navy-mid: #1f3b73;
    --navy-glow: #3358a0;
    --paper: #f2f2f2;
    --silver: #c9ced6;
    --silver-light: #eef0f3;
    --silver-dark: #8d939c;
    --ink: #2a2a2a;
    --on-navy: #e6e9ef;
  }
  * { margin: 0; padding: 0; box-sizing: border-box; }
  html, body { width: 1200px; height: 900px; overflow: hidden; }
  body {
    background: var(--backdrop);
    position: relative;
    font-family: "Tinos", "Times New Roman", serif;
  }
  .card {
    position: absolute;
    top: 291px;
    width: 520px;
    height: 318px;
    overflow: hidden;
  }
  /* Front side */
  .card-front {
    left: 50px;
    clip-path: polygon(0 14%, 8% 0, 100% 0, 100% 100%, 0 100%);
    background: radial-gradient(ellipse 60% 70% at 50% 35%, var(--navy-glow) 0%, var(--navy-mid) 45%, var(--navy-deep) 100%);
    text-align: center;
    color: var(--silver);
  }
  .front-mark {
    position: absolute;
    left: 50%;
    top: 40px;
    width: 92px;
    height: 92px;
    margin-left: -46px;
    border-radius: 50%;
    background: var(--silver);
  }
  .front-name {
    position: absolute;
    left: 0; right: 0;
    top: 150px;
    font-family: "Marcellus", "Times New Roman", serif;
    font-size: 27px;
    letter-spacing: 9px;
    color: var(--silver-light);
  }
  .front-subline {
    position: absolute;
    left: 72px; right: 72px;
    top: 186px;
    display: flex;
    align-items: center;
    gap: 12px;
  }
  .front-subline .rule {
    flex: 1;
    height: 1px;
    background: var(--silver-dark);
  }
  .front-chinese {
    font-family: "Noto Serif TC", serif;
    font-size: 24px;
    line-height: 30px;
    color: var(--silver-light);
  }
  .front-tagline {
    position: absolute;
    left: 0; right: 0;
    top: 236px;
    font-size: 19px;
    font-style: italic;
    color: var(--on-navy);
  }
  /* Back side */
  .card-back {
    left: 630px;
    clip-path: polygon(0 0, 90% 0, 100% 17%, 100% 100%, 0 100%);
    background: var(--paper);
  }
  .back-brand {
    position: absolute;
    left: 0; right: 0;
    top: 0;
    height: 158px;
    text-align: center;
    color: var(--ink);
  }
  .back-mark {
    position: absolute;
    left: 50%;
    top: 26px;
    width: 56px;
    height: 56px;
    margin-left: -28px;
    border-radius: 50%;
    background: var(--silver);
  }
  .back-name {
    position: absolute;
    left: 0; right: 0;
    top: 96px;
    font-family: "Marcellus", "Times New Roman", serif;
    font-size: 17px;
    letter-spacing: 6px;
  }
  .back-subline {
    position: absolute;
    left: 150px; right: 150px;
    top: 117px;
    display: flex;
    align-items: center;
    gap: 8px;
  }
  .back-subline .rule {
    flex: 1;
    height: 1px;
    background: var(--silver-dark);
  }
  .back-chinese {
    font-family: "Noto Serif TC", serif;
    font-size: 16px;
    line-height: 22px;
  }
  .back-band {
    position: absolute;
    left: 0; right: 0;
    top: 158px;
    height: 8px;
    background: linear-gradient(90deg, var(--silver-dark), var(--silver-light) 50%, var(--silver-dark));
  }
  .back-details {
    position: absolute;
    left: 0; right: 0;
    top: 166px;
    bottom: 0;
    background: radial-gradient(ellipse 55% 90% at 50% 100%, var(--navy-glow) 0%, var(--navy-mid) 45%, var(--navy-deep) 100%);
    color: var(--on-navy);
    text-align: center;
    padding-top: 14px;
    line-height: 1.3;
  }
  .person-name { font-size: 22px; }
  .person-name .chinese { font-family: "Noto Serif TC", serif; font-size: 13px; }
  .person-role { font-size: 14px; }
  .person-role .chinese { font-family: "Noto Serif TC", serif; font-size: 13px; }
  .contact-line { font-size: 13.5px; }
  .company-line { font-size: 13.5px; margin-top: 6px; }
</style>
</head>
<body>
  <section class="card card-front" aria-label="Business card front">
    <div class="front-mark"></div>
    <div class="front-name">LARCH VANTAGE</div>
    <div class="front-subline">
      <span class="rule"></span>
      <span class="front-chinese">林匯通</span>
      <span class="rule"></span>
    </div>
    <div class="front-tagline">“bring us a plan”</div>
  </section>

  <section class="card card-back" aria-label="Business card back">
    <div class="back-brand">
      <div class="back-mark"></div>
      <div class="back-name">LARCH VANTAGE</div>
      <div class="back-subline">
        <span class="rule"></span>
        <span class="back-chinese">林匯通</span>
        <span class="rule"></span>
      </div>
    </div>
    <div class="back-band"></div>
    <div class="back-details">
      <div class="person-name">Morris Pelham <span class="chinese">彭文德</span></div>
      <div class="person-role">Director <span class="chinese">董事</span></div>
      <div class="contact-line">mobile: 123 608 4471 &nbsp;email: mpelham@larchvantage.com</div>
      <div class="contact-line">www.larchvantage.com</div>
      <div class="company-line">Larch Vantage Pty. Ltd.</div>
      <div class="contact-line">Suite 27, 3-9 Quenby St. Elmvale NSW 2187</div>
    </div>
  </section>
</body>
</html>
```